お店の看板デザインを依頼させて頂きます。
看板は国道沿いに2つ、裏通りに1つ、スタンド看板1つを設置予定です。
スクールと共にサロン・ショップも展開している事が分かり、印象に残る様なデザインを希望します。
宜しくお願いいたします。
記載項目:電話番号 ・ロゴ・URL
ロゴはこちらのサイトで依頼、選定済(添付いたします)
URL 後日取得予定
看板は南北に走る国道に、北向きと西向きに一枚ずつ、裏通り東向きに一枚、スタンド看板の設置場所はお店の前か、国道から見える位置に置く予定です。

看板サイズ:国道沿い   H 2000 x W 1000 / H 2440 x W 1220
裏通り    H 910 x W 1820
スタンド看板 H 1300 x W 600
清潔、エレガント、高級なイメージを考えています
• 高解像度JPG (.jpg)
• イラストレーター形式 (.ai)
• フォトショップ形式 (.psd)
看板のデザインは縦型のもの1点でお願いします。
色はえんじ色でお願いします。

アロマテラピー(Aromatherapy)の文字を入れて頂き
アロマスクール(Aroma School)
ボディ&フェイシャル サロン(Body&Facial Salon)
アロマショップ(Aroma shop)
と入れて頂きたいです。
文字は英語でもカタカナでも両方使って頂いても構いません。

どうぞ宜しくお願いします。
たくさんのご提案ありがとうございます。

デザインの色ですが、えんじ色でと指定しておりましたが
ランサーさんからのご意見で、エレガント・高級感なら茶系が良いのでは…
とアドバイスいただきました。
確かにそうかもしれません。
私どもは素人ですので、プロの方のアドバイスは大変ありがたいです。

ですので、色はえんじには拘りません。
えんじを含め、他の色でも自由にデザインお願い致します。

どうぞ宜しくお願い致します。
たくさんの良いご提案をありがとうございます。

ご提案を拝見させて頂き、漠然としていたものが
だんだんと具体的にイメージ出来る様になって参りました。

前回、入れて頂きたい文言を挙げさせて頂きましたが
今回訂正し、以下のものを入れて頂きたいと思います。

Beauty&Body School
エステ・アロマテラピー・リフレクソロジー・ボディケア
Beauty&Body Salon
エステ・オイルトリートメント・リフレクソロジー・アロマテラピー
Aroma Shop
エッセンシャルオイル・ナチュラルオイル・ハーブウォーター

カタカナは英語よりも小さめでお願い致します。
字体はお任せいたします。

度々の追記で申し訳ありませんが、どうぞ宜しくお願い致します。

デザインの全体的なイメージが一つに偏らず、エステ・スクール・ショップのそれぞれにリンクしていた事。

縦長の看板がより良く生かされたデザインも気に入りました。

ご提案下さったランサーの皆さま、大変ありがとうございました。

たくさんのご提案に感謝致します。
また、機会がございましたら宜しくお願い致します。

```html
<!DOCTYPE html>
<html lang="ja">
<head>
<meta charset="utf-8">
<title>LUMA Beauty &amp; Body balance — Signboard</title>
<link href="https://fonts.googleapis.com/css2?family=Cinzel:wght@500&family=EB+Garamond:wght@400;500&family=Noto+Serif+JP:wght@400;500;700&family=Noto+Serif:wght@700&display=swap" rel="stylesheet">
<style>
  :root {
    --gold: #a8873a;
    --gold-dark: #8c6e26;
    --gold-light: #d2b86f;
    --cream: #f6efdc;
    --paper: #ffffff;
    --ink-light: #ffffff;
  }
  html, body {
    margin: 0;
    padding: 0;
    width: 1200px;
    height: 2400px;
    overflow: hidden;
    background: var(--paper);
  }
  .signboard {
    position: relative;
    width: 1200px;
    height: 2400px;
    background: var(--paper);
    overflow: hidden;
  }
  .rose-backdrop {
    position: absolute;
    inset: 0 0 572px 0;
    background: radial-gradient(ellipse at 30% 20%, var(--cream) 0%, rgba(246,239,220,0.35) 45%, rgba(255,255,255,0) 75%),
                radial-gradient(ellipse at 85% 65%, rgba(246,239,220,0.9) 0%, rgba(255,255,255,0) 55%);
  }
  .brand {
    position: absolute;
    top: 190px;
    left: 0;
    width: 100%;
    text-align: center;
    color: var(--gold);
  }
  .brand-name {
    font-family: "Cinzel", serif;
    font-weight: 500;
    font-size: 310px;
    line-height: 1;
    letter-spacing: 6px;
    margin: 0;
  }
  .brand-tagline {
    font-family: "EB Garamond", serif;
    font-size: 64px;
    margin: 30px 0 0;
    letter-spacing: 1px;
  }
  .feature-badge {
    position: absolute;
    top: 760px;
    left: 160px;
    width: 880px;
    height: 275px;
  }
  .feature-badge svg { position: absolute; inset: 0; }
  .feature-text {
    position: absolute;
    inset: 0;
    display: flex;
    flex-direction: column;
    align-items: center;
    justify-content: center;
    color: var(--ink-light);
  }
  .feature-kana {
    font-family: "Noto Serif JP", serif;
    font-size: 38px;
    letter-spacing: 4px;
    margin: 0 0 6px;
  }
  .feature-en {
    font-family: "EB Garamond", serif;
    font-size: 92px;
    line-height: 1;
    margin: 28px 0 0;
  }
  .services {
    position: absolute;
    top: 1160px;
    left: 130px;
    right: 100px;
    margin: 0;
    padding: 0;
    list-style: none;
    color: var(--gold);
  }
  .service { margin-bottom: 60px; }
  .service-title {
    display: flex;
    align-items: center;
    font-family: "EB Garamond", serif;
    font-size: 86px;
    line-height: 1.1;
    margin: 0;
  }
  .service-title svg { width: 52px; height: 52px; margin-right: 28px; flex: none; }
  .service-detail {
    font-family: "Noto Serif JP", serif;
    font-size: 26px;
    margin: 12px 0 0 80px;
    letter-spacing: 0;
    white-space: nowrap;
  }
  .contact-band {
    position: absolute;
    left: 0;
    bottom: 0;
    width: 100%;
    height: 572px;
    background: var(--gold);
    color: var(--ink-light);
  }
  .contact-band .band-trim { position: absolute; top: 36px; left: 0; width: 100%; height: 40px; }
  .contact-phone {
    position: absolute;
    top: 160px;
    width: 100%;
    text-align: center;
    font-family: "Noto Serif", serif;
    font-weight: 700;
    font-size: 124px;
    margin: 0;
    line-height: 1;
  }
  .contact-phone .label { font-size: 74px; margin-right: 24px; }
  .contact-url {
    position: absolute;
    top: 340px;
    width: 100%;
    text-align: center;
    font-family: "Noto Serif", serif;
    font-weight: 700;
    font-size: 78px;
    margin: 0;
    line-height: 1;
  }
</style>
</head>
<body>
<main class="signboard">
  <div class="rose-backdrop" role="img" aria-label="Faint cream rose pattern decorating the background"></div>

  <header class="brand">
    <h1 class="brand-name">LUMA</h1>
    <p class="brand-tagline">Beauty &amp; Body balance</p>
  </header>

  <section class="feature-badge">
    <svg viewBox="0 0 880 275" width="880" height="275" aria-hidden="true">
      <defs>
        <linearGradient id="badgeGold" x1="0" y1="0" x2="1" y2="1">
          <stop offset="0" stop-color="#8c6e26"/>
          <stop offset="0.45" stop-color="#d2b86f"/>
          <stop offset="1" stop-color="#8c6e26"/>
        </linearGradient>
      </defs>
      <ellipse cx="440" cy="137.5" rx="436" ry="133" fill="url(#badgeGold)"/>
      <ellipse cx="440" cy="137.5" rx="410" ry="112" fill="none" stroke="#ffffff" stroke-width="4" stroke-dasharray="2 10" stroke-linecap="round"/>
      <line x1="250" y1="135" x2="630" y2="135" stroke="#ffffff" stroke-width="3" stroke-dasharray="2 9" stroke-linecap="round"/>
    </svg>
    <div class="feature-text">
      <p class="feature-kana">アロマテラピー</p>
      <p class="feature-en">Aromatherapy</p>
    </div>
  </section>

  <ul class="services">
    <li class="service">
      <p class="service-title"><svg viewBox="-10 -10 20 20" aria-hidden="true"><g stroke="#a8873a" stroke-width="3.2" stroke-linecap="round"><line x1="0" y1="-9" x2="0" y2="9"/><line x1="-7.8" y1="-4.5" x2="7.8" y2="4.5"/><line x1="-7.8" y1="4.5" x2="7.8" y2="-4.5"/></g></svg>Beauty &amp; Body School</p>
      <p class="service-detail">エステ・アロマテラピー・リフレクソロジー・ボディケア</p>
    </li>
    <li class="service">
      <p class="service-title"><svg viewBox="-10 -10 20 20" aria-hidden="true"><g stroke="#a8873a" stroke-width="3.2" stroke-linecap="round"><line x1="0" y1="-9" x2="0" y2="9"/><line x1="-7.8" y1="-4.5" x2="7.8" y2="4.5"/><line x1="-7.8" y1="4.5" x2="7.8" y2="-4.5"/></g></svg>Beauty &amp; Body Salon</p>
      <p class="service-detail">エステ・オイルトリートメント・リフレクソロジー・アロマテラピー</p>
    </li>
    <li class="service">
      <p class="service-title"><svg viewBox="-10 -10 20 20" aria-hidden="true"><g stroke="#a8873a" stroke-width="3.2" stroke-linecap="round"><line x1="0" y1="-9" x2="0" y2="9"/><line x1="-7.8" y1="-4.5" x2="7.8" y2="4.5"/><line x1="-7.8" y1="4.5" x2="7.8" y2="-4.5"/></g></svg>Aroma shop</p>
      <p class="service-detail">エッセンシャルオイル・ナチュラルオイル・ハーブウォーター</p>
    </li>
  </ul>

  <footer class="contact-band">
    <svg class="band-trim" viewBox="0 0 1200 40" preserveAspectRatio="none" aria-hidden="true">
      <line x1="0" y1="6" x2="1200" y2="6" stroke="#ffffff" stroke-width="3"/>
      <line x1="0" y1="34" x2="1200" y2="34" stroke="#ffffff" stroke-width="3"/>
      <line x1="10" y1="20" x2="1200" y2="20" stroke="#ffffff" stroke-width="10" stroke-dasharray="10 22"/>
    </svg>
    <p class="contact-phone"><span class="label">Tel.</span>012-345-6789</p>
    <p class="contact-url">www.lumabeauty.jp</p>
  </footer>
</main>
</body>
</html>
```